Multi-Faceted Legal and Finanacial Advisory Group Needs Business Card Design

We need a business card design for a newly branded Orlando Florida area advising group consisting of Attorneys, Accountants and Financial Planners. The company is named TK Counsel Partners. You will find our initial work on a business card. The information on the business card are merely guideposts and not final product. The logo does not have the be the same as provided since we have not finalized the logo. We would like to stay with a black/white/grey color scheme, but limited use of color is not out of the question.

Target Market(s)

Businesses and their Corporate Representatives

Industry/Entity Type

Business

Contact Information for Business Card

Should have Name, Title, Phone, Cell, Fax, Email and website. Logo should incorporate TK in some fashion however final logo used does not have to be the one on the document provided.

Requirements
Must have
• An TK design on front and back.

```html
<!DOCTYPE html>
<html lang="en">
<head>
<meta charset="utf-8">
<title>TK Counsel Partners – Business Card</title>
<link rel="stylesheet" href="https://fonts.googleapis.com/css2?family=Michroma&display=swap">
<style>
  :root {
    --backdrop: #3b3b3d;
    --card: #ffffff;
    --ink: #0a0a0a;
    --band: #050505;
    --icon-grey: #5e5e5e;
    --rule-grey: #6a6a6a;
    --text-light: #ffffff;
  }
  * { margin: 0; padding: 0; box-sizing: border-box; }
  html, body {
    width: 1200px; height: 817px; overflow: hidden;
    background: var(--backdrop);
  }
  .card {
    position: absolute; left: 110px; top: 118px;
    width: 980px; height: 580px;
    background: var(--card);
    border-radius: 34px;
    overflow: hidden;
    font-family: "Michroma", "Arial", sans-serif;
    color: var(--ink);
  }
  .brand {
    position: absolute; left: 48px; top: 96px;
    display: flex; align-items: center; gap: 16px;
  }
  .brand-mark {
    width: 40px; height: 40px; flex: none;
    border-radius: 50%;
    background: var(--icon-grey);
  }
  .brand-name { font-size: 20px; color: var(--ink); white-space: nowrap; }
  .name-band {
    position: absolute; left: 0; top: 232px;
    width: 100%; height: 54px;
    background: var(--band);
    display: flex; align-items: center;
    padding-left: 44px;
    color: var(--text-light);
  }
  .name-band svg { width: 34px; height: 38px; margin-right: 20px; flex: none; }
  .person-name { font-size: 24px; letter-spacing: 1px; white-space: nowrap; }
  .name-divider { font-size: 24px; margin: 0 16px; }
  .person-title { font-size: 14px; letter-spacing: 1px; white-space: nowrap; }
  .contacts {
    position: absolute; left: 0; top: 300px;
    width: 100%; height: 160px;
    display: grid; grid-template-columns: 1fr 1fr 1fr;
  }
  .contact {
    display: flex; flex-direction: column; align-items: center; justify-content: center;
    gap: 22px;
    padding: 0 12px;
  }
  .contact + .contact { border-left: 3px solid var(--rule-grey); margin: 12px 0; }
  .contact-icon { width: 72px; height: 72px; }
  .contact-text { font-size: 17px; letter-spacing: 0.3px; white-space: nowrap; }
  .address-band {
    position: absolute; left: 0; top: 482px;
    width: 100%; height: 44px;
    background: var(--band);
    display: flex; align-items: center;
    padding-left: 44px;
    color: var(--text-light);
  }
  .address-band svg { width: 22px; height: 30px; margin-right: 18px; flex: none; }
  .address { font-size: 15px; letter-spacing: 1.5px; white-space: nowrap; }
</style>
</head>
<body>
  <main class="card">
    <div class="brand">
      <div class="brand-mark"></div>
      <span class="brand-name">TK Counsel Partners</span>
    </div>

    <div class="name-band">
      <svg viewBox="0 0 34 38" aria-hidden="true">
        <circle cx="17" cy="10" r="9" fill="#fff"/>
        <path d="M1 38 C1 26 8 21 17 21 C26 21 33 26 33 38 Z" fill="#fff"/>
      </svg>
      <span class="person-name">DANIEL REEVES</span>
      <span class="name-divider">|</span>
      <span class="person-title">GENERAL MANAGER</span>
    </div>

    <section class="contacts">
      <div class="contact">
        <svg class="contact-icon" viewBox="0 0 72 72" aria-hidden="true">
          <circle cx="36" cy="36" r="36" fill="var(--icon-grey)"/>
          <rect x="25" y="16" width="22" height="40" rx="4" fill="#fff"/>
          <rect x="28" y="22" width="16" height="25" fill="var(--icon-grey)"/>
          <circle cx="36" cy="51" r="2" fill="var(--icon-grey)"/>
        </svg>
        <span class="contact-text">407 555 0182</span>
      </div>
      <div class="contact">
        <svg class="contact-icon" viewBox="0 0 72 72" aria-hidden="true">
          <circle cx="36" cy="36" r="36" fill="var(--icon-grey)"/>
          <rect x="18" y="24" width="36" height="24" fill="#fff"/>
          <path d="M18 24 L36 38 L54 24" fill="none" stroke="var(--icon-grey)" stroke-width="2"/>
        </svg>
        <span class="contact-text">dreeves@tkcounsel.com</span>
      </div>
      <div class="contact">
        <svg class="contact-icon" viewBox="0 0 72 72" aria-hidden="true">
          <circle cx="36" cy="36" r="36" fill="var(--icon-grey)"/>
          <g fill="none" stroke="#fff" stroke-width="2.5">
            <circle cx="36" cy="36" r="18"/>
            <ellipse cx="36" cy="36" rx="8" ry="18"/>
            <line x1="18" y1="36" x2="54" y2="36"/>
            <line x1="36" y1="18" x2="36" y2="54"/>
            <path d="M21 27 H51 M21 45 H51"/>
          </g>
        </svg>
        <span class="contact-text">www.tkcounsel.com</span>
      </div>
    </section>

    <div class="address-band">
      <svg viewBox="0 0 22 30" aria-hidden="true">
        <path d="M11 0 C5 0 0 5 0 11 C0 19 11 30 11 30 C11 30 22 19 22 11 C22 5 17 0 11 0 Z" fill="#fff"/>
        <circle cx="11" cy="11" r="4" fill="var(--band)"/>
      </svg>
      <span class="address">210, 9th floor, Harbor Point Avenue ORL</span>
    </div>
  </main>
</body>
</html>
```